Need a business card for our overland brand!

We had the logo made and we need a great design for our business card. Use the logo provide or tweak it however you see fit.

Contact Information for Business Card

Name, Title, Telephone, email, website

```html
<!DOCTYPE html>
<html lang="en">
<head>
<meta charset="utf-8">
<title>Northpass Expeditions – Business Card</title>
<link rel="stylesheet" href="https://fonts.googleapis.com/css2?family=Josefin+Sans:wght@400;700&display=swap">
<style>
  :root {
    --backdrop: #2b2b2b;
    --card-blue: #1fa0c4;
    --pattern-blue: #2aa8ca;
    --white: #ffffff;
    --ink: #3a4152;
  }
  * { margin: 0; padding: 0; box-sizing: border-box; }
  html, body {
    width: 1090px;
    height: 1200px;
    overflow: hidden;
    background: var(--backdrop);
    font-family: "Josefin Sans", sans-serif;
  }
  .sheet {
    width: 1090px;
    height: 1200px;
    display: flex;
    flex-direction: column;
    align-items: center;
    justify-content: center;
    gap: 90px;
  }
  .card {
    position: relative;
    width: 780px;
    height: 444px;
    background: var(--card-blue);
    overflow: hidden;
    display: flex;
    flex-direction: column;
    align-items: center;
    justify-content: center;
    color: var(--white);
  }
  .card__pattern {
    position: absolute;
    inset: 0;
    background: linear-gradient(180deg, var(--pattern-blue), var(--card-blue));
    opacity: 0.55;
  }
  .card__content {
    position: relative;
    display: flex;
    flex-direction: column;
    align-items: center;
  }
  .brand-name {
    font-weight: 700;
    font-size: 66px;
    line-height: 1;
    text-transform: uppercase;
    text-align: center;
    letter-spacing: 1px;
    color: var(--white);
  }
  .brand-name span { display: block; }
  .brand-name span + span { margin-top: 10px; }
  .company-title {
    font-weight: 700;
    font-size: 31px;
    letter-spacing: 1.5px;
    text-transform: uppercase;
  }
  .contact-pill {
    margin-top: 30px;
    background: var(--white);
    color: var(--ink);
    border-radius: 12px;
    padding: 12px 20px 9px;
    font-size: 20px;
    font-weight: 400;
    display: flex;
    gap: 14px;
    align-items: center;
  }
  .contact-pill .divider { color: var(--ink); }
  .website {
    margin-top: 18px;
    font-size: 19px;
    font-weight: 700;
    letter-spacing: 0.5px;
  }
</style>
</head>
<body>
  <main class="sheet">
    <section class="card card--front">
      <div class="card__pattern" role="img" aria-label="Faint repeating pattern of small mountain-ridge lines across the card"></div>
      <div class="card__content">
        <h1 class="brand-name"><span>Northpass</span><span>Expeditions</span></h1>
      </div>
    </section>

    <section class="card card--back">
      <div class="card__pattern" role="img" aria-label="Faint repeating pattern of small mountain-ridge lines across the card"></div>
      <div class="card__content">
        <h2 class="company-title">Northpass Expeditions</h2>
        <p class="contact-pill">
          <span class="phone">+1 555 014 2290</span>
          <span class="divider">|</span>
          <span class="email">info@northpassexpeditions.com</span>
        </p>
        <p class="website">www.northpassexpeditions.com</p>
      </div>
    </section>
  </main>
</body>
</html>
```